HarborSlumber.com Trade Show banners

We need to do a design for 3 retractable banners that are 33" X 80" printed. The three banners will act as a back drop for our booth so there needs to be a left middle and a right, and fit together in a cohesive way. Our company is HarborSlumber.com, we make custom mattresses and bedding for boats. we've attached a few pictures to be featured in the design. Please pick and choose at your discretion for your layout, you do not need to use them all, we just want to give you options. Our logo should be large, spanning across the three banners. I've also included the winning brochure design from a couple of years ago, along with a 10X10 banner that was made to go along with it.

What we liked about the design was that it included imagery of boating/sailing along with or pictures and images. Although the colors in the 10X10 banner were a bit too dark. We would like the colors to be brighter and more vibrant in the design and catch customers eyes, while not overshadowing the photos or our logo etc.

As for copy we would like the following. Under our logo it should say: Custom Boat Mattresses and Bedding

We would also like to see the following tag lines included in the design:
Let's make your stateroom a STATEMENT ROOM!
A Fresh Approach to Stateroom Design
Boat Bedding Made EASY
Patterns on file for over 1000 different boats.

Please feel free to ask any question. We will be very responsive throughout the project and look forward to seeing your designs.

-Delia & Tobin
HarborSlumber.com

Target Market(s)

Men and women that own boats and yachts. Customers age range between Mid 30's to 80's

Industry/Entity Type

Marine

Font styles to use
Serif

Colors

Designer to choose colors to be used in the design.

Requirements
Must have
• The design should be very clean. While we included a lot of photos to choose from, less is more on a retractable banner. Pictures need to be visible from 10-12 feet away, as does text.
Nice to have
• It would be nice if the design shared some of the design elements of our website, but certainly it does not need nor should it be a copy of our home page.
Should not have
• The design should not be cluttered. It should not have text in the bottom 3rd of the banner.

```html
<!DOCTYPE html>
<html lang="en">
<head>
<meta charset="utf-8">
<title>HarborSlumber.com Trade Show Banners</title>
<link href="https://fonts.googleapis.com/css2?family=Alegreya:ital,wght@0,500;0,700;1,500&display=swap" rel="stylesheet">
<style>
:root{
  --stage:#5f5f5f;
  --navy:#1c2566;
  --royal:#2a43a0;
  --accent-red:#d6282f;
  --frame:#ffffff;
  --sky-top:#c9d3ea;
  --sky-mid:#e9e4ea;
  --haze:#d9c3b8;
  --sea-warm:#b98263;
  --sea-deep:#6d4a3e;
}
*{margin:0;padding:0;box-sizing:border-box}
html,body{width:1200px;height:926px;overflow:hidden;background:var(--stage)}
.stage{position:relative;width:1200px;height:926px}
.banner{position:absolute;top:77px;width:327px;height:793px;overflow:hidden}
.banner--left{left:72px}
.banner--middle{left:429px}
.banner--right{left:789px}
.banner__scene{position:absolute;inset:0;
  background:linear-gradient(180deg,var(--sky-top) 0%,var(--sky-mid) 30%,var(--haze) 48%,var(--sea-warm) 72%,var(--sea-deep) 100%)}
.banner--middle .banner__scene{background:linear-gradient(180deg,#bcc9e4 0%,#efe9e6 26%,#e6c9ad 50%,#c18660 74%,#7a5340 100%)}
.banner--right .banner__scene{background:linear-gradient(180deg,#c4cde6 0%,#f1e6dc 30%,#edc8a3 52%,#c98a5e 76%,#7a4f3b 100%)}
.brand{position:absolute;top:56px;left:0;right:0;display:flex;justify-content:center;align-items:center;gap:8px}
.brand__dot{width:34px;height:34px;border-radius:50%;background:var(--accent-red)}
.brand__name{font-family:"Alegreya",serif;font-weight:700;font-size:28px;color:var(--navy);letter-spacing:.2px}
.tagline{position:absolute;top:107px;left:0;right:0;text-align:center;font-family:"Alegreya",serif;font-style:italic;font-weight:500;font-size:16px;color:var(--royal)}
.headline{position:absolute;left:0;right:0;text-align:center;font-family:"Alegreya",serif;font-weight:500;font-size:27px;line-height:32px;color:var(--navy)}
.banner--left .headline{top:146px}
.banner--middle .headline,.banner--right .headline{top:162px}
.photo{position:absolute;left:46px;width:237px;height:148px;border:3px solid var(--frame)}
.photo--1{top:265px}.photo--2{top:420px}.photo--3{top:575px}
.photo--warm{background:linear-gradient(160deg,#8a3f24,#cbb9a4 55%,#6e2c1a)}
.photo--coral{background:linear-gradient(160deg,#a9c2d9,#d97c74 45%,#f0e4dc 70%,#c9564f)}
.photo--navy{background:linear-gradient(160deg,#e2a08a,#2b3566 55%,#1f2748)}
.photo--pattern{background:linear-gradient(160deg,#8b3a22,#c75a4a 40%,#7fa59a 70%,#b84b3c)}
.photo--slate{background:linear-gradient(160deg,#3c4048,#d8cbc0 50%,#8a3a22)}
.photo--white{background:linear-gradient(160deg,#2a2c30,#e9e7e4 50%,#4b4641)}
.photo--teal{background:linear-gradient(160deg,#b75a33,#2f7f87 55%,#1f5c63)}
.footer-line{position:absolute;top:750px;left:0;right:0;text-align:center;font-family:"Alegreya",serif;font-style:italic;font-weight:500;font-size:14px;color:#ffffff}
</style>
</head>
<body>
<main class="stage">
  <section class="banner banner--left">
    <div class="banner__scene" role="img" aria-label="Bright sky over a warm sunlit sea"></div>
    <div class="brand"><span class="brand__dot"></span><span class="brand__name">HarborSlumber.com</span></div>
    <p class="tagline">Custom Boat Mattresses and Bedding</p>
    <h2 class="headline">Let's make your<br>Stateroom a<br>STATEMENT ROOM!</h2>
    <div class="photo photo--1 photo--warm" role="img" aria-label="Yacht stateroom bed with a beige quilted cover and wood trim"></div>
    <div class="photo photo--2 photo--coral" role="img" aria-label="Bed with coral and white geometric comforter and blue headboard"></div>
    <div class="photo photo--3 photo--navy" role="img" aria-label="Navy quilted bed with coral patterned pillows"></div>
    <p class="footer-line">Patterns on file for over 1000 different boats.</p>
  </section>
  <section class="banner banner--middle">
    <div class="banner__scene" role="img" aria-label="Clouds and a sailboat sail above a golden sea"></div>
    <div class="brand"><span class="brand__dot"></span><span class="brand__name">HarborSlumber.com</span></div>
    <p class="tagline">Custom Boat Mattresses and Bedding</p>
    <h2 class="headline">Boat Bedding<br>Made EASY</h2>
    <div class="photo photo--1 photo--slate" role="img" aria-label="Stateroom bed with cream throw and fur pillows"></div>
    <div class="photo photo--2 photo--pattern" role="img" aria-label="Bed with red and teal ornamental print bedding"></div>
    <div class="photo photo--3 photo--navy" role="img" aria-label="Navy bed with anchor pillow and red cushions"></div>
    <p class="footer-line">Patterns on file for over 1000 different boats.</p>
  </section>
  <section class="banner banner--right">
    <div class="banner__scene" role="img" aria-label="Tall ship sails and rigging against a sunset sea"></div>
    <div class="brand"><span class="brand__dot"></span><span class="brand__name">HarborSlumber.com</span></div>
    <p class="tagline">Custom Boat Mattresses and Bedding</p>
    <h2 class="headline">A Fresh Approach to<br>Stateroom Design</h2>
    <div class="photo photo--1 photo--warm" role="img" aria-label="Custom quilted mattress in a wood-trimmed berth"></div>
    <div class="photo photo--2 photo--white" role="img" aria-label="White quilted custom mattress on a grey platform"></div>
    <div class="photo photo--3 photo--teal" role="img" aria-label="Teal quilted bed with striped and red pillows"></div>
    <p class="footer-line">Patterns on file for over 1000 different boats.</p>
  </section>
</main>
</body>
</html>
```